依頼詳細
●デザインの要望
・少し温かみ、やわらかさのあるデザイン(まるっこすぎない)
※参考例:poruくらいのやわらかさ
・そのほかの色については特に指定なし(現在の青は入れなくてOKです)
⇒カラフルにするかどうかもデザインの中で考えて頂いて結構です
・現在のアプリにある下記のボタンを全て実装する
※投稿ボタン、画面更新ボタン、履歴ボタン、オプションボタン、カテゴリ選択ボタン の5個
・投稿が表示されるマス目は正方形だけでなく長方形等もまぜてほしい
※現在は正方形オンリーですが、縦に2個くっつけたものや横に2個くっつけたものが入ってきたりするデザイン
⇒アプリ:Tiledeck の記事一覧画面のようなイメージ
・zelvonなのでzvos7のフラットなイメージ(がっつり立体的にはしてほしくないです)

●納品物
PSDファイル1個(zelvonで使用する倍のサイズの 1920x1280 くらいで作ってください)
可能であればレイヤーのあるPNGファイル(可能であればで結構です)

サイトURL
https://apps.trovenlo.jp/jp/app/id518203764?mt=8
ページ数
1ページ
希望イメージ
シンプル 複雑
単色 カラフル
暗い 明るい
日常 高級
遊び心 厳粛
未来的 伝統的
女性的 男性的
希望する色
小豆色や薄い茶色等温かみのある色全般
納品ファイル
• フォトショップ形式 (.psd)
• PNG形式 (.png)
補足説明
■ 選んだ理由

やわらかいテイストでかつ既存の青をさし色に入れて頂けたこと、
またプラスアルファとしてスプラッシュスクリーンをご提示いただけたため、
より実装後のアプリのイメージがわくことができました。

■ 提案者全員のお礼・コメント

たくさんのご提案ありがとうございました。
特にUIそのものまで提案して頂けたりと非常にこちらとしても勉強になる案件となりました。

上部のバーのデザインや、吹き出し型のデザイン、カラフル、マット等
かなり悩ませていただきました。
最終的にはより女性的で、かつ落ち着いている
という部分を基準に選ぶことにしました。

本アプリは今後もどんどん改良を加える予定のため、
また機会が有りましたら是非宜しくお願い致します。

```html
<!DOCTYPE html>
<html lang="ja">
<head>
<meta charset="utf-8">
<title>タイル投稿一覧</title>
<link rel="stylesheet" href="https://fonts.googleapis.com/css2?family=Noto+Sans+JP:wght@400;500&display=swap">
<style>
  :root{
    --orange:#f29a1f;
    --orange-deep:#e9801a;
    --orange-grad-top:#f6ac3a;
    --peach:#fde4c4;
    --cream:#fff6ea;
    --white:#ffffff;
    --text-orange:#e98a25;
    --text-brown:#b85e14;
    --bar:#e8781a;
    --bar-line:#f3a35a;
    --status:#f7f7f7;
  }
  *{box-sizing:border-box;margin:0;padding:0}
  html,body{width:800px;height:1200px;overflow:hidden;background:var(--white)}
  body{font-family:"Noto Sans JP",sans-serif;position:relative}
  .status-bar{position:absolute;left:0;top:0;width:800px;height:53px;background:var(--status);
    display:flex;align-items:center;justify-content:space-between;padding:0 14px;font-size:28px;color:#222}
  .status-left{display:flex;align-items:center;gap:12px}
  .signal{display:flex;gap:4px}
  .signal i{width:10px;height:10px;border-radius:50%;background:#222;display:block}
  .signal i.off{background:none;border:2px solid #222}
  .status-time{font-weight:500;position:absolute;left:50%;transform:translateX(-50%)}
  .status-right{display:flex;align-items:center;gap:12px}
  .battery{width:52px;height:24px;border:2px solid #222;border-radius:4px;padding:2px;position:relative}
  .battery::after{content:"";position:absolute;right:-6px;top:6px;width:3px;height:8px;background:#222}
  .battery span{display:block;width:40%;height:100%;background:#222}
  .tile-grid{position:absolute;left:0;top:53px;width:800px;height:987px;overflow:hidden}
  .tile{position:absolute;overflow:hidden;padding:22px 20px;font-size:26px;line-height:1.38;color:var(--text-orange);
    border-right:2px solid var(--white);border-bottom:2px solid var(--white)}
  .tile--orange{background:linear-gradient(to bottom,var(--orange-grad-top),var(--orange));color:var(--text-brown)}
  .tile--orange-bright{background:linear-gradient(to bottom,var(--orange-grad-top),var(--orange-deep));color:var(--white)}
  .tile--peach{background:var(--peach)}
  .tile--cream{background:var(--cream)}
  .tile--white{background:var(--white)}
  .tile--cut{text-align:right;padding-left:4px;padding-right:14px}
  .tile--cut-right{padding-right:0;white-space:nowrap}
  .tool-bar{position:absolute;left:0;top:1040px;width:800px;height:160px;background:var(--bar);display:flex}
  .tool{flex:1;display:flex;align-items:center;justify-content:center;border-right:2px solid var(--bar-line);color:var(--white)}
  .tool:last-child{border-right:none}
  .tool svg{width:78px;height:78px}
  .tool-label{font-size:40px;letter-spacing:14px;font-weight:500}
</style>
</head>
<body>
  <header class="status-bar">
    <div class="status-left">
      <div class="signal"><i></i><i></i><i></i><i class="off"></i><i class="off"></i></div>
      <span class="carrier">kiro</span>
    </div>
    <div class="status-time">22:29</div>
    <div class="status-right">
      <span>⏰</span><span>✱</span><div class="battery"><span></span></div>
    </div>
  </header>

  <main class="tile-grid">
    <article class="tile tile--orange tile--cut" style="left:0;top:0;width:139px;height:227px">部長にプ<br>部式まし</article>
    <article class="tile tile--orange" style="left:139px;top:0;width:256px;height:227px">どっちがどっちかわからん</article>
    <article class="tile tile--peach" style="left:395px;top:0;width:258px;height:480px">何度も笑って 何度も泣いて 何度も考えて 何度も間違って 何度も緊張して 何度も苦しくなって 何度も夢みて 何度も切なくなっただけどどんなに苦しくても一度も諦めようなんて思わなかった。好きっていう気持ちに嘘つきたくなかった</article>
    <article class="tile tile--white tile--cut-right" style="left:653px;top:0;width:147px;height:227px">マロは変わり<br>でおじゃる</article>

    <article class="tile tile--orange tile--cut" style="left:0;top:227px;width:139px;height:253px">やったこと<br>驚いた</article>
    <article class="tile tile--cream" style="left:139px;top:227px;width:256px;height:253px">感情的な高ぶりを抑えたい</article>
    <article class="tile tile--cream tile--cut-right" style="left:653px;top:227px;width:147px;height:253px">白け犬だ<br>続けてあき<br>けていた</article>

    <article class="tile tile--white" style="left:0;top:480px;width:395px;height:254px;padding-left:10px">子は「3月14日」にプロポーズする…その理由は単にホワイトデーだからではなく、円周率「3.14」が永遠に続くので、二人の愛が永遠に続くように…という意味が込められている</article>
    <article class="tile tile--orange-bright" style="left:395px;top:480px;width:405px;height:254px;padding-right:0">嫉妬するのは簡単だけど、憧れるのは難しい。「会いたい」と思うのは簡単だけど、「会いたい」と言うのは難しい。</article>

    <article class="tile tile--peach tile--cut" style="left:0;top:734px;width:139px;height:253px">の履歴欄に<br>年4月 部社<br>てます</article>
    <article class="tile tile--orange" style="left:139px;top:734px;width:256px;height:253px">お金がない</article>
    <article class="tile tile--cream" style="left:395px;top:734px;width:258px;height:253px">ミルカソーダ当たり缶引いたwwww</article>
    <article class="tile tile--cream tile--cut-right" style="left:653px;top:734px;width:147px;height:253px">明日から頑張<br>を信じてい</article>
  </main>

  <nav class="tool-bar">
    <div class="tool tool--post" aria-label="投稿">
      <svg viewBox="0 0 40 40" fill="none" stroke="#fff" stroke-width="3" stroke-linejoin="round">
        <path d="M8 32 L10 24 L27 7 L33 13 L16 30 Z"/><path d="M24 10 L30 16"/>
      </svg>
    </div>
    <div class="tool tool--refresh" aria-label="更新">
      <svg viewBox="0 0 40 40" fill="none" stroke="#fff" stroke-width="6" stroke-linecap="butt">
        <path d="M31 21 A11 11 0 1 1 25 10.5"/><path d="M21 4 L31 10 L22 16 Z" fill="#fff" stroke="none"/>
      </svg>
    </div>
    <div class="tool tool--history" aria-label="履歴">
      <svg viewBox="0 0 40 40" fill="none" stroke="#fff" stroke-width="2.5">
        <rect x="9" y="4" width="22" height="32"/>
        <path d="M13 11H27M13 16H27M13 21H27M13 26H27M13 31H23"/>
      </svg>
    </div>
    <div class="tool tool--option" aria-label="オプション">
      <svg viewBox="0 0 40 40">
        <g fill="#fff">
          <circle cx="20" cy="20" r="11"/>
          <g id="teeth"><rect x="17" y="3" width="6" height="8"/><rect x="17" y="29" width="6" height="8"/><rect x="3" y="17" width="8" height="6"/><rect x="29" y="17" width="8" height="6"/></g>
          <use href="#teeth" transform="rotate(45 20 20)"/>
        </g>
        <circle cx="20" cy="20" r="5" fill="#e8781a"/>
      </svg>
    </div>
    <div class="tool tool--category"><span class="tool-label">全体</span></div>
  </nav>
</body>
</html>
```